Healthy Food Healthy Brain Rack Card

We want a new 2 page (front and page) 3.67" x 8.5" rack card. This rack card is the first of a series we are creating. We will have five more eventually.

The minimum font size for the text on the front is 11 point and also for other main body text.

Use the text on the word document.

The images and layout in the word document are just sample ideas we had.

We have a subscripton to adobe stock images so prefer to get images from there or free high quality images.

The document is for older readers. Do not put text over graphics and keep it simple and easy to read with high contrast.

We are open to any color scheme, though something that conveys fresh and healthy, is good.

We want some very simple design element(s) incorporated that convey Native American communities or heritage. But NO head dress, teepee graphics, etc.

At the top, of the first page we would like a collage of healthy food images. This can include fish, chicken, fresh vegetables, berries, brown rice, etc.

On the back side, the text below the brown box on the word document with the title "mock up" can be smaller as needed.

Please remember to include the funding statement - it can be in a very small font 6/7 point.

For more information about our project, please visit https://velmorcollective.org/mind-care/

```html
<!DOCTYPE html>
<html lang="en">
<head>
<meta charset="utf-8">
<title>Healthy Food Healthy Brain Rack Card</title>
<link rel="stylesheet" href="https://fonts.googleapis.com/css2?family=PT+Sans+Narrow:wght@400;700&family=Montserrat:wght@800&family=Passion+One:wght@400;700&family=Oswald:wght@600&display=swap">
<style>
  :root {
    --teal: #5ba3aa;
    --teal-dark: #4a9199;
    --maroon: #5c2326;
    --ink: #1d1d1d;
    --pink: #efd3d3;
    --white: #ffffff;
    --backdrop: #e3e3e3;
  }
  * { margin: 0; padding: 0; box-sizing: border-box; }
  html, body { width: 1200px; height: 1200px; overflow: hidden; }
  body { background: var(--backdrop); position: relative; font-family: "PT Sans Narrow", sans-serif; color: var(--ink); }

  .card { position: absolute; top: 128px; width: 407px; height: 944px; background: var(--white); overflow: hidden; }
  .card--front { left: 151px; }
  .card--back { left: 630px; }
  .abs { position: absolute; }
  .center { text-align: center; left: 0; width: 100%; }
  .shape-layer { position: absolute; left: 0; top: 0; width: 407px; height: 944px; }

  /* Recipe side */
  .recipe-photo { position: absolute; left: 0; top: 0; width: 407px; height: 230px; }
  .brand-seal { position: absolute; left: 290px; top: 120px; width: 78px; height: 40px; display: flex; align-items: center; justify-content: center; font-family: "Oswald", sans-serif; font-weight: 600; font-size: 20px; color: var(--maroon); }
  .recipe-title { top: 186px; font-family: "Montserrat", sans-serif; font-weight: 800; font-size: 16.5px; line-height: 22px; letter-spacing: 0.4px; }
  .make-home { top: 234px; font-family: "Passion One", sans-serif; font-weight: 700; font-size: 28px; color: var(--teal); letter-spacing: 0.6px; }
  .ingredients { left: 25px; top: 289px; width: 359px; height: 110px; background: var(--maroon); border-radius: 14px; color: var(--white); font-size: 15px; line-height: 20.5px; }
  .ingredients-pill { left: 129px; top: 276px; width: 150px; height: 32px; background: var(--white); border-radius: 16px; border: 2px solid var(--maroon); color: var(--teal); font-family: "Oswald", sans-serif; font-weight: 600; font-size: 20px; line-height: 28px; text-align: center; }
  .ingredients ul { list-style: none; position: absolute; }
  .ing-col1 { left: 12px; top: 20px; }
  .ing-col1 li:last-child { line-height: 17px; }
  .ing-col2 { left: 166px; top: 30px; }
  .ing-col3 { left: 264px; top: 30px; }
  .method { left: 23px; top: 410px; width: 360px; font-size: 15px; line-height: 20.5px; text-align: justify; text-align-last: center; }
  .community-note { left: 26px; top: 534px; width: 353px; height: 99px; border: 1.5px dashed var(--maroon); border-radius: 12px; padding: 10px 14px 0; font-weight: 700; font-size: 15px; line-height: 20.5px; text-align: center; }
  .more-label { font-size: 13.5px; line-height: 17px; }
  .more-head { font-family: "Oswald", sans-serif; font-weight: 600; font-size: 14.5px; color: var(--maroon); letter-spacing: 0.3px; line-height: 18px; }
  .url-bar { position: absolute; background: var(--pink); font-size: 14px; line-height: 20px; text-align: center; }
  .partner { left: 112px; top: 846px; display: flex; align-items: center; gap: 8px; }
  .partner-dot { width: 36px; height: 36px; border-radius: 50%; background: var(--teal); }
  .partner-name { font-family: "PT Sans Narrow", sans-serif; font-weight: 700; font-size: 14px; line-height: 15px; color: var(--teal); width: 130px; }
  .funding { left: 23px; top: 898px; width: 362px; font-size: 6.5px; line-height: 8.6px; color: var(--ink); }

  /* Brain health side */
  .org-mark { left: 30px; top: 30px; display: flex; align-items: center; gap: 12px; }
  .org-dot { width: 46px; height: 46px; border-radius: 50%; background: var(--maroon); }
  .org-rule { width: 1.5px; height: 56px; background: var(--maroon); }
  .org-name { font-family: "Oswald", sans-serif; font-weight: 600; font-size: 30px; line-height: 32px; color: var(--white); letter-spacing: 0.5px; }
  .headline { font-family: "Passion One", sans-serif; font-weight: 700; font-size: 43px; line-height: 41px; letter-spacing: 1px; }
  .headline-food { top: 364px; color: var(--teal); }
  .headline-brain { top: 405px; color: var(--maroon); }
  .intro { left: 24px; top: 455px; width: 356px; font-size: 15px; line-height: 15.5px; text-align: justify; }
  .steps-label { left: 24px; top: 530px; font-size: 15px; }
  .steps { list-style: none; position: absolute; font-size: 15px; line-height: 20.5px; }
  .steps li { position: relative; padding-left: 18px; margin-bottom: 7px; }
  .steps svg { position: absolute; left: 0; top: 5px; width: 11px; height: 11px; }
  .steps-left { left: 28px; top: 560px; width: 182px; }
  .steps-right { left: 214px; top: 560px; width: 180px; }
  .closing { left: 24px; top: 785px; font-size: 15px; }
  .call-pill { left: 61px; top: 847px; width: 288px; height: 29px; background: var(--white); border-radius: 15px; display: flex; align-items: center; font-family: "PT Sans Narrow", sans-serif; font-weight: 700; font-size: 22px; color: var(--ink); }
  .call-pill span:first-child { width: 98px; text-align: center; border-right: 1.5px solid var(--ink); }
  .call-pill span:last-child { flex: 1; text-align: center; }
  .office { top: 878px; width: 150px; color: var(--white); font-size: 14px; line-height: 17px; text-align: center; }
  .office-title { color: #e9f3f4; }
  .office-hq { left: 52px; }
  .office-nm { left: 205px; }
  .office-rule { left: 203px; top: 882px; width: 1px; height: 54px; background: var(--white); }
</style>
</head>
<body>

<!-- Recipe side -->
<section class="card card--front">
  <svg class="shape-layer" viewBox="0 0 407 944" aria-hidden="true">
    <rect x="0" y="0" width="407" height="230" fill="#8d7a68"/>
    <path d="M0,222 C60,180 170,168 270,168 C290,120 330,110 355,125 C378,135 395,165 407,185 L407,944 L0,944 Z" fill="#ffffff"/>
    <path d="M0,872 C90,895 200,900 280,885 C330,875 375,862 407,850 L407,944 L0,944 Z" fill="var(--teal)"/>
  </svg>
  <div class="recipe-photo" role="img" aria-label="Grilled salmon with roasted potatoes, tomatoes and greens on a dark plate"
       style="height:190px;background:radial-gradient(ellipse at 45% 55%, #c86a3c 0%, #a5542f 30%, #6e5a48 65%, rgba(141,122,104,0) 90%);clip-path:polygon(0 0,100% 0,100% 80%,70% 88%,0 100%);"></div>
  <div class="brand-seal">Velmor</div>

  <h1 class="abs center recipe-title">GRILLED SALMON &amp;<br>VEGGIE FOIL PACKETS</h1>
  <h2 class="abs center make-home">MAKE THIS AT HOME</h2>

  <div class="abs ingredients">
    <ul class="ing-col1"><li>Salmon</li><li>Asparagus</li><li>Red or Green Peppers</li><li>(Or any seasonal vegetable)</li></ul>
    <ul class="ing-col2"><li>Onion</li><li>Lemon – sliced</li><li>Basil</li></ul>
    <ul class="ing-col3"><li>Olive Oil</li><li>Salt and Pepper</li><li>Garlic Powder</li></ul>
  </div>
  <div class="abs ingredients-pill">INGREDIENTS:</div>

  <p class="abs method">Cut asparagus, peppers, and onion into bite-size pieces. Cut salmon into 4-6 oz pieces. Tear tin foil large enough to wrap around salmon &amp; veggies (2 layers). Add veggies and salmon to foil. Drizzle with olive oil, season with salt, pepper, basil, garlic &amp; top with a piece of sliced lemon. Wrap foil tightly around food. Grill at 400 degrees for about 20 minutes.</p>

  <p class="abs community-note">Food &amp; drink are a source of strength and connection to community. A return to traditional food pathways and eating local, seasonal fresh foods make healthier eating easier.</p>

  <p class="abs center more-label" style="top:647px;">For More Information</p>
  <h3 class="abs center more-head" style="top:665px;">ABOUT HEALTHIER EATING</h3>
  <p class="abs center more-label" style="top:686px;">PlateWise Guide</p>
  <div class="url-bar" style="left:96px;top:711px;width:215px;">https://www.platewiseguide.org</div>
  <h3 class="abs center more-head" style="top:731px;">ABOUT BRAIN HEALTH</h3>
  <p class="abs center more-label" style="top:751px;">Native Elder Brain Resource Hub</p>
  <div class="url-bar" style="left:86px;top:770px;width:235px;">https://www.nativeelderbrainhub.org</div>
  <p class="abs center more-label" style="top:794px;">Regional Memory Health Program</p>
  <div class="url-bar" style="left:86px;top:815px;width:235px;">https://www.memoryhealthprogram.org</div>

  <div class="abs partner">
    <div class="partner-dot"></div>
    <div class="partner-name">Native Elder Brain Resource Hub</div>
  </div>

  <p class="abs funding">This product is supported by the Office of Community Health Grants (OCHG) as part of a financial assistance award totaling $348,711 with 100 percent funded by OCHG. The contents are those of the author(s) and do not necessarily represent the official views of, nor an endorsement by, OCHG or any government agency. For more about our project, visit https://velmorcollective.org/mind-care/</p>
</section>

<!-- Brain health side -->
<section class="card card--back">
  <svg class="shape-layer" viewBox="0 0 407 944" aria-hidden="true">
    <rect x="0" y="0" width="407" height="944" fill="#ffffff"/>
    <path d="M0,0 H407 V108 C300,85 160,80 80,108 C45,120 15,140 0,160 Z" fill="var(--teal)"/>
    <path d="M0,835 C90,830 170,838 250,825 C320,815 370,808 407,797 V944 H0 Z" fill="var(--teal)"/>
  </svg>
  <svg class="shape-layer" viewBox="0 0 407 944" role="img" aria-label="Bowl of grilled chicken, green peppers, cherry tomatoes, brown rice, mushrooms and spinach">
    <defs>
      <linearGradient id="bowlTones" x1="0" y1="0" x2="1" y2="1">
        <stop offset="0" stop-color="#c9d6b0"/>
        <stop offset="0.35" stop-color="#d6493a"/>
        <stop offset="0.6" stop-color="#5da23a"/>
        <stop offset="1" stop-color="#d9b07a"/>
      </linearGradient>
    </defs>
    <path d="M0,205 C30,150 110,110 230,100 C300,95 370,110 407,125 V235 C360,250 300,300 230,330 C170,355 80,360 40,335 C15,315 0,280 0,250 Z" fill="url(#bowlTones)"/>
  </svg>

  <div class="abs org-mark">
    <div class="org-dot"></div>
    <div class="org-rule"></div>
    <div class="org-name">VELMOR<br>COLLECTIVE</div>
  </div>

  <h1 class="abs center headline headline-food">HEALTHY FOOD</h1>
  <h1 class="abs center headline headline-brain">HEALTHY BRAIN</h1>

  <p class="abs intro">Everyone slows down as they get older, both in body and mind. Eating healthier food can help your overall health, including brain health. It may also reduce your risk for memory loss and problems thinking.</p>

  <p class="abs steps-label">Healthier steps to protect your brain:</p>

  <ul class="steps steps-left">
    <li><svg viewBox="0 0 12 12"><circle cx="6" cy="6" r="5.2" fill="none" stroke="var(--teal)" stroke-width="1"/><path d="M3.5,6.2 L5.3,7.9 L8.6,4.4" fill="none" stroke="var(--teal)" stroke-width="1.2"/></svg>Eat more vegetables, fruits, whole grains, and lower-fat milk</li>
    <li><svg viewBox="0 0 12 12"><circle cx="6" cy="6" r="5.2" fill="none" stroke="var(--teal)" stroke-width="1"/><path d="M3.5,6.2 L5.3,7.9 L8.6,4.4" fill="none" stroke="var(--teal)" stroke-width="1.2"/></svg>Use less salt and added sugar</li>
    <li><svg viewBox="0 0 12 12"><circle cx="6" cy="6" r="5.2" fill="none" stroke="var(--teal)" stroke-width="1"/><path d="M3.5,6.2 L5.3,7.9 L8.6,4.4" fill="none" stroke="var(--teal)" stroke-width="1.2"/></svg>Eat more fish, chicken, turkey, beans, and nuts</li>
    <li><svg viewBox="0 0 12 12"><circle cx="6" cy="6" r="5.2" fill="none" stroke="var(--teal)" stroke-width="1"/><path d="M3.5,6.2 L5.3,7.9 L8.6,4.4" fill="none" stroke="var(--teal)" stroke-width="1.2"/></svg>Cut down on bad fats (“saturated” and trans), cholesterol, and red meat</li>
  </ul>
  <ul class="steps steps-right">
    <li><svg viewBox="0 0 12 12"><circle cx="6" cy="6" r="5.2" fill="none" stroke="var(--teal)" stroke-width="1"/><path d="M3.5,6.2 L5.3,7.9 L8.6,4.4" fill="none" stroke="var(--teal)" stroke-width="1.2"/></svg>Buy fresh, not packaged food when you can</li>
    <li><svg viewBox="0 0 12 12"><circle cx="6" cy="6" r="5.2" fill="none" stroke="var(--teal)" stroke-width="1"/><path d="M3.5,6.2 L5.3,7.9 L8.6,4.4" fill="none" stroke="var(--teal)" stroke-width="1.2"/></svg>Limit how much alcohol you drink</li>
    <li><svg viewBox="0 0 12 12"><circle cx="6" cy="6" r="5.2" fill="none" stroke="var(--teal)" stroke-width="1"/><path d="M3.5,6.2 L5.3,7.9 L8.6,4.4" fill="none" stroke="var(--teal)" stroke-width="1.2"/></svg>Learn your daily calorie needs for your body size</li>
    <li><svg viewBox="0 0 12 12"><circle cx="6" cy="6" r="5.2" fill="none" stroke="var(--teal)" stroke-width="1"/><path d="M3.5,6.2 L5.3,7.9 L8.6,4.4" fill="none" stroke="var(--teal)" stroke-width="1.2"/></svg>Take care of your mental and spiritual health to support your physical and brain health</li>
  </ul>

  <p class="abs closing">Small changes can make a big difference for better brain health.</p>

  <div class="abs call-pill"><span>Call Us:</span><span>(555) 214-0398</span></div>

  <div class="abs office office-hq"><div class="office-title">Headquarters Office:</div>2480 Cedar Ridge Rd #210<br>Fairbrook, MD 20915</div>
  <div class="abs office-rule"></div>
  <div class="abs office office-nm"><div class="office-title">New Mexico Office:</div>715 Mesa Hollow Dr, NE<br>Alba Vista, NM 87120</div>
</section>

</body>
</html>
```